Banner for promote service of debit card

We are PagaVelo and we need the banners to be posted on the facebook and instagram pages.
We want something to communicate that it is an exclusive debit card full of services.
Low commissions.
Our competitors:
https://www.nortapay-pagos.it/it/home.html
https://www.zelkor-conti.it/it/
https://www.fotoreelz.it/serravanbank/
sendquillo
maybe some banner that makes the idea of a convenient debit card that everyone can use.
Girls enjoying card shopping.
Please check also website for slogans and phrases to use
https://www.pagavelo-carta.it/
Should show the services.
We must convey that it is a fast, simple card that guarantees privacy.
We need strong banners that attract people as these ban will be sponsored on instagram and facebook
Target Market(s)
People 18-35 y
Open Bank account. low commissions. Easy to use. No limits. 100% Privacy.
Requirements
Must have
- Written in Italian.

```html
<!DOCTYPE html>
<html lang="it">
<head>
<meta charset="utf-8">
<title>PagaVelo – Banner social</title>
<link href="https://fonts.googleapis.com/css2?family=Montserrat:wght@300;400;600;800&display=swap" rel="stylesheet">
<style>
  :root {
    --magenta: #c42394;
    --white: #ffffff;
    --sun: #fbc54a;
    --lilac: #b197d6;
    --lagoon: #58cad6;
    --mist: #eef2ec;
    --sand: #f6e3d1;
    --mint: #e4fbef;
    --logo-dot: #f0563f;
    --logo-text: #6b5a66;
  }
  * { box-sizing: border-box; margin: 0; padding: 0; }
  html, body {
    width: 1200px; height: 1000px; overflow: hidden;
    background: var(--white);
    font-family: "Montserrat", sans-serif;
  }
  .board { position: relative; width: 1200px; height: 1000px; }

  .banner {
    position: absolute; width: 553px; height: 290px; overflow: hidden;
    --pill: var(--white);
  }
  .banner--sun    { left: 34px;  top: 39px;  --accent: var(--sun);    --photo-a: #f3df86; --photo-b: #f0c64e; }
  .banner--lilac  { left: 612px; top: 38px;  --accent: var(--lilac);  --photo-a: #c7a3dc; --photo-b: #d9566a; }
  .banner--lagoon { left: 34px;  top: 357px; --accent: var(--lagoon); --photo-a: #6ccfd8; --photo-b: #e2703a; --pill: var(--mint); }
  .banner--mist   { left: 614px; top: 357px; --accent: var(--mist);   --photo-a: #eef0ea; --photo-b: #e7b6a6; }
  .banner--sand   { left: 336px; top: 674px; --accent: var(--sand);   --photo-a: #e9c7a8; --photo-b: #d88aa3; }

  .banner__art { position: absolute; inset: 0; width: 100%; height: 100%; }
  .art-accent { fill: var(--accent); }
  .art-magenta { fill: var(--magenta); }
  .art-pill { fill: var(--pill); }
  .stop-a { stop-color: var(--photo-a); }
  .stop-b { stop-color: var(--photo-b); }

  .logo-tab {
    position: absolute; right: 0; width: 76px; height: 38px;
    background: var(--white); border-radius: 20px 0 0 20px;
    display: flex; align-items: center; justify-content: center; gap: 4px;
  }
  .logo-tab--top { top: 14px; }
  .logo-tab--bottom { top: 233px; }
  .logo-tab__dot { width: 7px; height: 7px; border-radius: 50%; background: var(--logo-dot); }
  .logo-tab__name { font-size: 8px; font-weight: 600; color: var(--logo-text); }

  .copy {
    position: absolute; right: 23px; text-align: right; color: var(--white);
  }
  .copy--dark { color: var(--magenta); }
  .copy__title { font-weight: 800; letter-spacing: -0.2px; }
  .copy__lead { font-weight: 800; font-size: 13.5px; margin-top: 4px; }
  .copy__body { font-weight: 400; font-size: 13px; line-height: 17.5px; }
  .copy__body--light { font-weight: 300; font-size: 13.5px; margin-top: 2px; }

  .banner--sun .copy { top: 105px; }
  .banner--sun .copy__title { font-size: 30px; line-height: 40px; }

  .banner--lilac .copy, .banner--lagoon .copy { top: 102px; }
  .banner--lilac .copy__title, .banner--lagoon .copy__title { font-size: 19px; line-height: 23px; margin-bottom: 7px; }

  .banner--mist .copy { top: 104px; }
  .banner--mist .copy__title { font-size: 20px; line-height: 24px; margin-bottom: 4px; }

  .banner--sand .copy { top: 84px; }
  .banner--sand .copy__title { font-size: 20px; line-height: 24px; margin-bottom: 7px; }
</style>
</head>
<body>
<main class="board">

  <section class="banner banner--sun">
    <svg class="banner__art" viewBox="0 0 968 508" preserveAspectRatio="none">
      <defs><linearGradient id="photo-sun" x1="0" y1="0" x2="1" y2="1"><stop offset="0" class="stop-a"/><stop offset="1" class="stop-b"/></linearGradient></defs>
      <rect class="art-accent" width="968" height="508"/>
      <circle class="art-magenta" cx="227" cy="254" r="443"/>
      <rect class="art-accent" x="290" y="162" width="678" height="188"/>
      <circle role="img" aria-label="Foto: ragazza in camicia gialla che tiene una carta davanti all'occhio" fill="url(#photo-sun)" cx="290" cy="254" r="232"/>
      <rect class="art-pill" x="-40" y="125" width="105" height="55" rx="27.5"/>
      <circle class="art-pill" cx="120" cy="152" r="27"/>
      <rect class="art-pill" x="-40" y="235" width="76" height="55" rx="27.5"/>
      <rect class="art-pill" x="64" y="235" width="126" height="55" rx="27.5"/>
      <rect class="art-pill" x="-40" y="345" width="150" height="55" rx="27.5"/>
    </svg>
    <div class="logo-tab logo-tab--top"><span class="logo-tab__dot"></span><span class="logo-tab__name">PagaVelo</span></div>
    <div class="copy">
      <h2 class="copy__title">All in one.</h2>
      <p class="copy__lead">La carta adatta alla tue esigenze:</p>
      <p class="copy__body copy__body--light">Veloce, Internazionale, Semplice.</p>
    </div>
  </section>

  <section class="banner banner--lilac">
    <svg class="banner__art" viewBox="0 0 968 508" preserveAspectRatio="none">
      <defs><linearGradient id="photo-lilac" x1="0" y1="0" x2="0" y2="1"><stop offset="0" class="stop-a"/><stop offset="1" class="stop-b"/></linearGradient></defs>
      <rect class="art-accent" width="968" height="508"/>
      <circle class="art-magenta" cx="227" cy="254" r="443"/>
      <rect class="art-accent" x="290" y="162" width="678" height="188"/>
      <circle role="img" aria-label="Foto: ragazza con cappello di paglia che regge borse della spesa colorate" fill="url(#photo-lilac)" cx="290" cy="254" r="232"/>
      <rect class="art-pill" x="-40" y="125" width="105" height="55" rx="27.5"/>
      <circle class="art-pill" cx="120" cy="152" r="27"/>
      <rect class="art-pill" x="-40" y="235" width="76" height="55" rx="27.5"/>
      <rect class="art-pill" x="64" y="235" width="126" height="55" rx="27.5"/>
      <rect class="art-pill" x="-40" y="345" width="150" height="55" rx="27.5"/>
    </svg>
    <div class="logo-tab logo-tab--top"><span class="logo-tab__dot"></span><span class="logo-tab__name">PagaVelo</span></div>
    <div class="copy">
      <h2 class="copy__title">Enjoy your cart,<br>Fai quello che vuoi!</h2>
      <p class="copy__body">Privacy garantita, credito assicurato.<br>Senza essere controllato!</p>
    </div>
  </section>

  <section class="banner banner--lagoon">
    <svg class="banner__art" viewBox="0 0 968 508" preserveAspectRatio="none">
      <defs><linearGradient id="photo-lagoon" x1="1" y1="0" x2="0" y2="1"><stop offset="0" class="stop-a"/><stop offset="1" class="stop-b"/></linearGradient></defs>
      <rect class="art-accent" width="968" height="508"/>
      <circle class="art-magenta" cx="227" cy="254" r="443"/>
      <rect class="art-accent" x="290" y="162" width="678" height="188"/>
      <circle role="img" aria-label="Foto: ragazza in maglia arancione che paga con la carta al terminale POS" fill="url(#photo-lagoon)" cx="290" cy="254" r="232"/>
      <rect class="art-pill" x="-40" y="125" width="105" height="55" rx="27.5"/>
      <circle class="art-pill" cx="120" cy="152" r="27"/>
      <rect class="art-pill" x="-40" y="235" width="76" height="55" rx="27.5"/>
      <rect class="art-pill" x="64" y="235" width="126" height="55" rx="27.5"/>
      <rect class="art-pill" x="-40" y="345" width="150" height="55" rx="27.5"/>
    </svg>
    <div class="logo-tab logo-tab--top"><span class="logo-tab__dot"></span><span class="logo-tab__name">PagaVelo</span></div>
    <div class="copy">
      <h2 class="copy__title">La carta adatta<br>alla tue esigenze:</h2>
      <p class="copy__body">Transazioni istantanee, costi bassi<br>e facile da ricaricare.</p>
    </div>
  </section>

  <section class="banner banner--mist">
    <svg class="banner__art" viewBox="0 0 968 508" preserveAspectRatio="none">
      <defs><linearGradient id="photo-mist" x1="0" y1="1" x2="1" y2="0"><stop offset="0" class="stop-a"/><stop offset="1" class="stop-b"/></linearGradient></defs>
      <rect class="art-accent" width="968" height="508"/>
      <circle class="art-magenta" cx="227" cy="254" r="443"/>
      <rect class="art-accent" x="290" y="162" width="678" height="188"/>
      <circle role="img" aria-label="Foto: mano che mostra una carta di pagamento rossa" fill="url(#photo-mist)" cx="290" cy="254" r="232"/>
      <rect class="art-pill" x="-40" y="125" width="105" height="55" rx="27.5"/>
      <circle class="art-pill" cx="120" cy="152" r="27"/>
      <rect class="art-pill" x="-40" y="235" width="76" height="55" rx="27.5"/>
      <rect class="art-pill" x="64" y="235" width="126" height="55" rx="27.5"/>
      <rect class="art-pill" x="-40" y="345" width="150" height="55" rx="27.5"/>
    </svg>
    <div class="logo-tab logo-tab--bottom"><span class="logo-tab__dot"></span><span class="logo-tab__name">PagaVelo</span></div>
    <div class="copy copy--dark">
      <h2 class="copy__title">Una carta per tutti.</h2>
      <p class="copy__body">Le nostre carte non hanno nessun limite,<br>decidi tu come e quando usarle,<br>tutte le tue necessità in un'unica soluzione!</p>
    </div>
  </section>

  <section class="banner banner--sand">
    <svg class="banner__art" viewBox="0 0 968 508" preserveAspectRatio="none">
      <defs><linearGradient id="photo-sand" x1="0" y1="0" x2="1" y2="1"><stop offset="0" class="stop-a"/><stop offset="1" class="stop-b"/></linearGradient></defs>
      <rect class="art-accent" width="968" height="508"/>
      <circle class="art-magenta" cx="227" cy="254" r="443"/>
      <rect class="art-accent" x="290" y="162" width="678" height="188"/>
      <circle role="img" aria-label="Foto: coppia sorridente in bicicletta con cappelli di paglia e fiori nel cestino" fill="url(#photo-sand)" cx="290" cy="254" r="232"/>
      <rect class="art-pill" x="-40" y="125" width="105" height="55" rx="27.5"/>
      <circle class="art-pill" cx="120" cy="152" r="27"/>
      <rect class="art-pill" x="-40" y="235" width="76" height="55" rx="27.5"/>
      <rect class="art-pill" x="64" y="235" width="126" height="55" rx="27.5"/>
      <rect class="art-pill" x="-40" y="345" width="150" height="55" rx="27.5"/>
    </svg>
    <div class="logo-tab logo-tab--bottom"><span class="logo-tab__dot"></span><span class="logo-tab__name">PagaVelo</span></div>
    <div class="copy copy--dark">
      <h2 class="copy__title">La libertà a<br>portata di click.</h2>
      <p class="copy__body">Acquista ovunque senza limiti,<br>Senza controllo di solidità<br>finanziaria né reddito<br>dimostrabile.</p>
    </div>
  </section>

</main>
</body>
</html>
```